Business card design and logo needed - Photographer

I take photos of weddings, rodeos, snowmobiling.
Need a card to hand out to prospective clients.
Industry/Entity Type
Business
Contact Information for Business Card
Marcus Dolven Photography
Requirements
Must have
- Bold
Black or white base.
My website. www.MarcusDolven.example
Should not have
- camera/ lens/ aperture blades

```html
<!DOCTYPE html>
<html lang="en">
<head>
<meta charset="utf-8">
<title>Marcus Dolven Photography – Business Card</title>
<link rel="stylesheet" href="https://fonts.googleapis.com/css2?family=Teko:wght@400;500;600&display=swap">
<style>
  :root {
    --page: #ffffff;
    --card: #000000;
    --ink: #ffffff;
  }
  * { margin: 0; padding: 0; box-sizing: border-box; }
  html, body {
    width: 1200px;
    height: 693px;
    overflow: hidden;
    background: var(--page);
  }
  .card {
    position: absolute;
    left: 28px;
    top: 28px;
    width: 1153px;
    height: 640px;
    background: var(--card);
    color: var(--ink);
    font-family: "Teko", "Arial Narrow", sans-serif;
    text-align: center;
  }
  .brand-name {
    position: absolute;
    left: 0;
    right: 0;
    top: 185px;
    font-weight: 600;
    font-size: 104px;
    line-height: 1;
    letter-spacing: 0.01em;
    text-transform: uppercase;
  }
  .headline {
    position: absolute;
    left: 0;
    right: 0;
    top: 415px;
    font-weight: 600;
    font-size: 56px;
    line-height: 1;
    letter-spacing: 0.005em;
    text-transform: uppercase;
  }
  .contact {
    position: absolute;
    left: 0;
    right: 0;
    font-weight: 500;
    font-size: 15px;
    line-height: 1;
    letter-spacing: 0.62em;
    text-transform: uppercase;
  }
  .contact--phone { top: 470px; }
  .contact--web { top: 494px; }
</style>
</head>
<body>
  <main class="card">
    <div class="brand-name">Marcus Dolven</div>
    <h1 class="headline">Marcus Dolven Photography</h1>
    <p class="contact contact--phone">(306) 555 0142</p>
    <p class="contact contact--web">www.MarcusDolven.example</p>
  </main>
</body>
</html>
```